Bramblewood Lodging letterhead

We need a letterhead designed that includes the new logo that has just been designed for our business. The letterhead will need to be formatted for digital use as well as for print.

Target Market(s)

Private tenant, corporate tenants, real estate agents

Industry/Entity Type

Digital

Requirements
Must have
• ABN 87 592 104 316
PO Box 7816, Tilbury Mail Centre QLD 4792
Email: dorian.platt@quillmail.net
Ph: 0438 172 964

```html
<!DOCTYPE html>
<html lang="en">
<head>
<meta charset="utf-8">
<title>Bramblewood Lodging Letterhead</title>
<link href="https://fonts.googleapis.com/css2?family=Oswald:wght@600&family=Open+Sans:wght@400&display=swap" rel="stylesheet">
<style>
  :root {
    --backdrop: #a9a8a6;
    --paper: #ffffff;
    --brand: #7a2b27;
    --ink: #2e2e2e;
  }
  html, body {
    margin: 0;
    padding: 0;
    width: 1200px;
    height: 711px;
    overflow: hidden;
    background: var(--backdrop);
  }
  .canvas {
    position: relative;
    width: 1200px;
    height: 711px;
  }
  .letterhead {
    position: absolute;
    top: 30px;
    left: 370px;
    width: 460px;
    height: 651px;
    background: var(--paper);
    box-shadow: 0 2px 10px rgba(0, 0, 0, 0.18);
  }
  .brand {
    position: absolute;
    top: 40px;
    right: 34px;
    display: flex;
    align-items: center;
    gap: 8px;
  }
  .brand-mark {
    width: 40px;
    height: 40px;
    background: var(--brand);
    border-radius: 4px;
  }
  .brand-name {
    font-family: "Oswald", sans-serif;
    font-weight: 600;
    font-size: 19px;
    line-height: 19px;
    text-transform: uppercase;
    color: var(--brand);
    letter-spacing: 0.3px;
  }
  .contact {
    position: absolute;
    top: 92px;
    right: 34px;
    width: 150px;
    margin: 0;
    font-family: "Open Sans", sans-serif;
    font-size: 7.5px;
    line-height: 10.5px;
    color: var(--ink);
    font-style: normal;
  }
  .contact span {
    display: block;
  }
</style>
</head>
<body>
  <main class="canvas">
    <section class="letterhead">
      <header class="brand">
        <div class="brand-mark"></div>
        <div class="brand-name">Bramblewood<br>Lodging</div>
      </header>
      <address class="contact">
        <span>ABN 87 592 104 316</span>
        <span>PO Box 7816,</span>
        <span>Tilbury Mail Centre QLD 4792</span>
        <span>Email: dorian.platt@quillmail.net</span>
        <span>Ph: 0438 172 964</span>
      </address>
    </section>
  </main>
</body>
</html>
```